Talvex Engineering Business card Design

We need to make business cards for our NDT and inspection company. The company is called Talvex Engineering. We want a professional modern feel business card. We have just completed the remaking of our website and would like to have business cards with the same feel and colours. The final design should communicate professionalism and cutting edge tech.

Target Market(s)

We sell to B2B Business clients. Our customer is an engineer or decision maker in the mechanical engineering / Oil and gas field.

Contact Information for Business Card

Please see the current business cards that we have uploaded to get the details. You can also look at our Website www.talvex-eng.example for more.

Requirements
Must have
• Less is more
Nice to have
• Less is more

```html
<!DOCTYPE html>
<html lang="en">
<head>
<meta charset="utf-8">
<title>Talvex Engineering Business Card</title>
<link href="https://fonts.googleapis.com/css2?family=Montserrat:wght@600&family=Work+Sans:wght@400&family=Fira+Sans:wght@500&display=swap" rel="stylesheet">
<style>
  :root {
    --navy: #1f2f63;
    --red: #a80e12;
    --ink: #4a4a4a;
    --white: #ffffff;
    --backdrop: #2a2a2a;
  }
  * { box-sizing: border-box; margin: 0; padding: 0; }
  html, body { width: 1200px; height: 900px; overflow: hidden; }
  body { background: var(--backdrop); position: relative; font-family: "Work Sans", sans-serif; }

  .card {
    position: absolute;
    left: 261px;
    width: 656px;
    height: 357px;
    border-radius: 28px;
    overflow: hidden;
    box-shadow: 0 6px 14px rgba(0,0,0,0.45);
  }
  .card-front { top: 69px; background: var(--white); }
  .card-back { top: 472px; background: var(--red); }

  .header-band {
    position: absolute;
    left: 0; top: 0;
    width: 100%;
    height: 108px;
    background: linear-gradient(180deg, var(--navy) 0%, var(--navy) 55%, #5a1f3e 80%, var(--red) 100%);
  }

  .brand {
    position: absolute;
    left: 26px;
    top: 134px;
    display: flex;
    align-items: center;
    gap: 10px;
  }
  .brand-dot { width: 26px; height: 26px; border-radius: 50%; background: var(--red); }
  .brand-name {
    font-family: "Montserrat", sans-serif;
    font-weight: 600;
    font-size: 19px;
    color: var(--navy);
  }

  .holder { position: absolute; right: 29px; top: 186px; text-align: right; }
  .holder-name {
    font-family: "Montserrat", sans-serif;
    font-weight: 600;
    font-size: 23px;
    letter-spacing: 0.5px;
    color: var(--navy);
    line-height: 1;
  }
  .holder-role { font-size: 17px; color: var(--ink); margin-top: 6px; letter-spacing: 0.5px; }

  .divider { position: absolute; left: 26px; width: 601px; top: 243px; height: 1.5px; background: var(--red); }

  .contact-list { position: absolute; left: 26px; top: 270px; list-style: none; }
  .contact-list li {
    display: flex; align-items: center; gap: 8px;
    font-size: 17px; color: var(--ink); line-height: 22px; letter-spacing: 0.4px;
  }
  .contact-icon { width: 11px; height: 11px; flex: none; }
  .web-accent { color: var(--red); }

  .address {
    position: absolute; right: 27px; top: 292px; text-align: right;
    font-size: 17px; color: var(--ink); line-height: 22px; letter-spacing: 0.4px;
  }

  .edge-tab { position: absolute; right: 0; top: 192px; width: 8px; height: 37px; background: var(--red); }

  .service-list {
    position: absolute; top: 113px; list-style: none;
    font-family: "Fira Sans", sans-serif; font-weight: 500;
    font-size: 17.5px; color: var(--white); line-height: 22.8px;
  }
  .service-list.left { left: 38px; }
  .service-list.right { left: 372px; }
  .service-list li { display: flex; align-items: center; gap: 12px; }
  .service-list li::before {
    content: ""; width: 10px; height: 10px; border-radius: 50%; background: var(--white); flex: none;
  }
</style>
</head>
<body>

<section class="card card-front">
  <div class="header-band" role="img" aria-label="Decorative header area in navy and red"></div>

  <div class="brand">
    <span class="brand-dot"></span>
    <span class="brand-name">Talvex Engineering</span>
  </div>

  <div class="holder">
    <p class="holder-name">DANIEL ROSS</p>
    <p class="holder-role">Director</p>
  </div>

  <div class="divider"></div>

  <ul class="contact-list">
    <li>
      <svg class="contact-icon" viewBox="0 0 12 12"><path fill="var(--navy)" d="M2.5 0.5 L4.5 0.5 L5 3 L3.7 4 C4.4 5.8 6 7.4 8 8.2 L9 7 L11.5 7.5 L11.5 9.5 C11.5 10.8 10.5 11.5 9.5 11.5 C4.5 11 1 7.5 0.5 2.5 C0.5 1.4 1.3 0.5 2.5 0.5 Z"/></svg>
      +330 2460-5193
    </li>
    <li>
      <svg class="contact-icon" viewBox="0 0 12 12"><rect x="0.8" y="2.2" width="10.4" height="7.6" fill="none" stroke="var(--navy)" stroke-width="1.4"/><path d="M1 2.6 L6 6.6 L11 2.6" fill="none" stroke="var(--navy)" stroke-width="1.4"/></svg>
      info@talvex-eng.example
    </li>
    <li>
      <svg class="contact-icon" viewBox="0 0 12 12"><g fill="none" stroke="var(--navy)" stroke-width="1"><circle cx="6" cy="6" r="5.2"/><ellipse cx="6" cy="6" rx="2.3" ry="5.2"/><path d="M0.8 6 H11.2 M1.6 3.4 H10.4 M1.6 8.6 H10.4"/></g></svg>
      <span>www.<span class="web-accent">talvex-eng</span>.example</span>
    </li>
  </ul>

  <p class="address">2750 Harbor<br>Street Kelso, 98626</p>

  <div class="edge-tab"></div>
</section>

<section class="card card-back">
  <ul class="service-list left">
    <li>API 653 Tank Inspections</li>
    <li>API 570 Pipeline Inspections</li>
    <li>API 510 Pressure Vessel Inspections</li>
    <li>Welding Inspection</li>
    <li>Electrical Inspection</li>
    <li>OCTG Inspections</li>
  </ul>
  <ul class="service-list right">
    <li>Liting Equipment Inspections</li>
    <li>Non-Destructive Testing</li>
    <li>UT / PT /MT /RT / VT</li>
    <li>Advanced NDT</li>
    <li>PAUT / MFL / ILI</li>
    <li>Engineering Projects</li>
  </ul>
</section>

</body>
</html>
```